Printed Circuit Boards Company Brochure Design Project

We are seeking a design of a professional brochure for our company. The company will contain information on the attached documents. The audience will be our prospective customers who are buyers of our printed circuit boards. The brochure should have three languages namely, English, Chinese and Japanese. The brochure will contain some technical details information of our current manufacturing capability. The key message is we are an organization that embraces excellence and customer satisfaction is our number one priority. As to the color scheme, we are opened even though our logo attached is green which is made of printed circuit boards. I like to have the brochure put some emphasis on our "EXCELLENCE" concept.

I have uploaded a fourth file which contains the Chinese translation. I like the brochure to have three languages. I will enclose the Japanese version tomorrow. Thanks. Arlo

I have posted an updated Japanese translation. Please incorporate Japanese into the design together with English and Chinese.  Use your imagination to present the brochure in a way that it is elegant to present the three languages. The take away of our company is we are committed to be a "credible" printed circuit board suppliers, starting from single sided PCB to multilayered PCB. We would like the audience to "feel" safe to buy from us as we are credible to make sure they have the lowest risks of procuring from us.

I have updated new brochure file in English, Chinese and Japanese. The changes I made is to eliminate the service section and move the original service contents to product section below the double sided and multilayered printed circuit boards.

I need the technical capability information be handled as an insert.

The brochure should contain some pockets to allows us to put a name card and other presentation materials.

buyers of printed circuit boards

It Company

• three languages, namely English , Chinese and Japanese.

```html
<!DOCTYPE html>
<html lang="en">
<head>
<meta charset="utf-8">
<title>Kestrel International Limited – Brochure</title>
<link href="https://fonts.googleapis.com/css2?family=Noto+Serif:wght@400;700&family=Noto+Serif+SC:wght@400;700&family=Noto+Serif+JP:wght@400;700&family=Roboto+Condensed:wght@700&display=swap" rel="stylesheet">
<style>
:root{
  --bg:#ece8e1;
  --pcb-dark:#0f2621;
  --pcb:#173a32;
  --pcb-mid:#1f4d42;
  --green:#2e6b3a;
  --gold:#c9a43a;
  --gold-light:#f4e9b8;
  --paper:#ffffff;
  --ink:#2a2a2a;
  --ink-light:#d8ddd9;
  --rule:#b9b9b9;
}
*{box-sizing:border-box;margin:0;padding:0}
html,body{width:1200px;height:933px;overflow:hidden;background:var(--bg)}
body{position:relative;font-family:"Noto Serif",serif;color:var(--ink)}

/* front cover */
.cover{position:absolute;left:28px;top:190px;width:400px;height:560px;overflow:hidden;background:var(--pcb-dark);box-shadow:0 6px 18px rgba(0,0,0,.25)}
.cover-pattern{position:absolute;inset:0;background:radial-gradient(circle at 30% 30%,var(--pcb-mid),var(--pcb-dark) 70%)}
.cover-band{position:absolute;left:-60px;top:330px;width:560px;height:120px;transform:rotate(-24deg);background:linear-gradient(180deg,var(--gold) 0%,var(--gold-light) 55%,#fff 100%);display:flex;align-items:center;justify-content:center}
.cover-name{font-family:"Roboto Condensed",sans-serif;font-weight:700;color:var(--pcb);font-size:30px;letter-spacing:1px;line-height:1;text-align:center}

/* inside spread */
.spread{position:absolute;left:456px;top:130px;width:720px;height:650px;display:flex;box-shadow:0 6px 18px rgba(0,0,0,.25)}
.page{position:relative;width:240px;height:100%;overflow:hidden}
.page-dark{background:var(--pcb-dark);padding:14px 12px}
.page-light{background:var(--paper);padding:22px 16px;border-left:1px solid #e3e3e3}

.photo{width:100%;height:128px;margin-bottom:10px;background:linear-gradient(160deg,#cfd6d3,#8e9a95);border:2px solid #0a1a16}
.contact{display:flex;gap:8px;margin-top:10px;font-size:6.3px;line-height:1.45;color:var(--ink-light)}
.contact div{flex:1;min-width:0;overflow-wrap:anywhere}
.contact .zh{font-family:"Noto Serif SC",serif}

h2{font-family:"Roboto Condensed",sans-serif;font-weight:700;color:var(--green);font-size:9px;letter-spacing:.3px;margin:10px 0 5px}
h2.zh{font-family:"Noto Serif SC",serif;font-weight:400;text-decoration:underline}
h2.ja{font-family:"Noto Serif JP",serif;font-weight:400;text-decoration:underline}
.page-light p{font-size:6.8px;line-height:1.7;margin-bottom:6px}
.page-light p.zh{font-family:"Noto Serif SC",serif}
.page-light p.ja{font-family:"Noto Serif JP",serif}
.section-rule{border:0;border-top:1px solid var(--rule);margin:14px 0 4px}

.principles{padding-right:36px}
.principles h2{text-transform:uppercase}
.principles h3{font-family:"Roboto Condensed",sans-serif;font-size:6.8px;color:var(--green);margin:5px 0 2px;text-transform:uppercase}
.principles p{font-size:6.2px;line-height:1.55;margin-bottom:4px}
.capability{width:100%;border-collapse:collapse;font-size:5.8px;margin:6px 0}
.capability td{border:1px solid #555;padding:3px;vertical-align:top;line-height:1.45}
.customers{display:grid;grid-template-columns:repeat(3,1fr);gap:5px;margin-top:6px}
.customer-mark{height:12px;background:#c8cfcc}
.customer-mark.round{width:12px;border-radius:50%;background:#d24b3a}

.tabs{position:absolute;right:0;top:150px;width:28px;display:flex;flex-direction:column;gap:8px}
.tab{height:110px;background:var(--green);color:#fff;font-family:"Roboto Condensed",sans-serif;font-weight:700;font-size:10px;letter-spacing:2px;writing-mode:vertical-rl;display:flex;align-items:center;justify-content:center}
.page-band{position:absolute;right:0;bottom:90px;width:28px;height:70px;background:linear-gradient(180deg,var(--gold),var(--gold-light))}
</style>
</head>
<body>

<section class="cover" aria-label="Front cover">
  <div class="cover-pattern" role="img" aria-label="Dark green printed circuit board pattern"></div>
  <div class="cover-band"><div class="cover-name">KESTREL<br>International Limited</div></div>
</section>

<section class="spread" aria-label="Inside pages">
  <article class="page page-dark">
    <div class="photo" role="img" aria-label="Factory photo: operator at a board production line"></div>
    <div class="photo" role="img" aria-label="Factory photo: plating and etching machinery"></div>
    <div class="photo" role="img" aria-label="Factory photo: technician at an inspection station"></div>
    <div class="contact">
      <div>
        Hong Kong Business Office:<br>Kestrel International Limited<br>45/F, Harbour Court,<br>18 Cedar Avenue,<br>Bay Point, Hong Kong<br>Telephone: (852) 3000-1100<br>Fax: (852) 3000-1122<br>Email: sales@kestrelboard.example<br><br>
        China Factory:<br>Kestrel International (Riverbend) Limited<br>9 Willow South 2 Road,<br>138 Industrial District,<br>Lakeview Town, Riverbend,<br>Guangdong Province, China<br>Telephone: (86) 700-0000-1200<br>Fax: (86) 700-0000-1211
      </div>
      <div class="zh">
        香港聯絡辦事處:<br>紅隼國際有限公司<br>港灣閣四十五樓<br>柏樹道十八號<br>灣景香港<br>電話: (852) 3000-1100<br>傳真: (852) 3000-1122<br>電郵:<br>sales@kestrelboard.example<br><br>
        中國工廠:<br>紅隼國際(河灣)有限公司<br>中國廣東省河灣市<br>湖景鎮138工業區<br>柳岸南二路九號<br>電話: (86) 700-0000-1200<br>傳真: (86) 700-0000-1211
      </div>
    </div>
  </article>

  <article class="page page-light">
    <h2>Background</h2>
    <p>Kestrel International Limited (KIL) was set up in Hong Kong in 2007 by two Hong Kong entrepreneurs, Mr. Dane Holloway and Mr. Arlo Petrov. We acquired the single sided printed circuit board factory located in Riverbend City, Guangdong Province, China, from Halden Corporation of the U.S. in 2007. In addition to KIL, Mr. Holloway and Mr. Petrov also own Northvale Technology Company Limited (www.northvale-flex.example), a semiconductor company based in Hong Kong since 1997 with a total investment of over US$100 million. Northvale is engaged in the manufacturing of flexible substrates and the assembly of Micro Electro Mechanical Systems (MEMS).</p>
    <p>KIL has been awarded TS 16949 and ISO14000 certificates since 2009 and 2004 respectively.</p>
    <hr class="section-rule">
    <h2 class="zh">我們的背景</h2>
    <p class="zh">紅隼國際有限公司(KIL)二零零七年成立於香港,同年從美國海登公司收購了位於廣東省河灣市的單面印刷電路板工廠。公司股東亦擁有北谷科技有限公司,一家自一九九七年成立於香港的半導體公司,投資總額超過一億美元,從事柔性基材製造及微機電系統裝配。</p>
    <hr class="section-rule">
    <h2 class="ja">我々の背景</h2>
    <p class="ja">紅隼国際有限公司(KIL)は2007年に香港で設立しました。同年、アメリカのハルデン社から広東省河湾市の片面印刷配線板工場を買収しました。株主は1997年に香港で設立した半導体会社も所有し、投資総額は1億米ドルを超えております。</p>
  </article>

  <article class="page page-light principles">
    <h2>Business Principles</h2>
    <p>KIL strives to be a professional and credible printed circuit board supplier. We embrace "EXCELLENCE" in product quality, service and on time delivery, building long term partnerships with every customer.</p>
    <h2>Products</h2>
    <h3>Single Layered Printed Circuit Boards</h3>
    <p>We offer single layered boards through our own production facility to serve customers in consumer, industrial and automotive markets.</p>
    <h3>Double Layered and Multi-Layered Printed Circuit Boards</h3>
    <p>Through trusted partners we supply double sided and multilayer boards with 100% electrical testing and full traceability.</p>
    <table class="capability">
      <tr><td>Consistent quality</td><td>All facilities hold TS16949 and ISO14000 and are audited yearly.</td></tr>
      <tr><td>Product delivery on time</td><td>Our staff track every order daily and report status to customers.</td></tr>
    </table>
    <h2>Customers</h2>
    <p>Due to our quality, service and delivery, we serve a number of large Japanese and US customers, which include:</p>
    <div class="customers" role="img" aria-label="Customer brand marks">
      <div class="customer-mark"></div><div class="customer-mark round"></div><div class="customer-mark"></div>
      <div class="customer-mark"></div><div class="customer-mark"></div><div class="customer-mark round"></div>
      <div class="customer-mark"></div><div class="customer-mark"></div><div class="customer-mark"></div>
    </div>
    <div class="tabs">
      <div class="tab">ENGLISH</div>
      <div class="tab">CHINESE</div>
      <div class="tab">JAPANESE</div>
    </div>
    <div class="page-band"></div>
  </article>
</section>

</body>
</html>
```